Flyer for American Indian Elders on Dementia Warning Signs

We need a flyer designed for older adults who are American Indian or Alaska Native (in the U.S.).

Ideally, the flyer should complement the colors of our logos. The project logo and our organization logo are attached to the brief.

When people see the flyer we want them to feel that it represents their culture, is warm, and professional but relatable to older adults and people who have limited incomes.

I have attached an earlier draft of the document we designed ourselves BUT we want different and better.

It is for older adults who have trouble reading so:
1. you must use a font that is 11.5 points or larger
2. Do not put text over complex pictures or use shading with words
3. You can use a serif font for the heading, but should use san serif for the body text
4. There should be good contrast between the font color and background

Please do not use any images that include a head dress or pictures of American Indian people or things that are very traditional or "token" imagery.

We need to save a small space under the call out box/ somewhere on the flyer for other people to add their logo once they download.

Let us know if you have questions or need additional information.

Target Market(s)

Older American Indian people

Font styles to use
Serif
Sans Serif

Requirements
Must have
• Easy to read for older adults
Should not have
• indian headdress

```html
<!DOCTYPE html>
<html lang="en">
<head>
<meta charset="utf-8">
<title>10 Signs of Thinking or Memory Changes that Might be Dementia</title>
<link rel="stylesheet" href="https://fonts.googleapis.com/css2?family=Roboto+Condensed:wght@400;700&display=swap">
<style>
  :root {
    --navy: #0b1733;
    --teal: #4fa8b1;
    --teal-light: #a9d3d8;
    --teal-pale: #e6f2f3;
    --white: #ffffff;
    --slot: #dae5e9;
    --slot-text: #9aa9b0;
    --accent: #c0564a;
  }
  * { box-sizing: border-box; margin: 0; padding: 0; }
  html, body { width: 927px; height: 1200px; overflow: hidden; background: var(--white); }
  body { font-family: "Roboto Condensed", "Arial Narrow", sans-serif; color: var(--navy); }
  .flyer { position: relative; width: 927px; height: 1200px; overflow: hidden; }

  .masthead { position: absolute; left: 0; top: 0; width: 927px; height: 167px; background: var(--navy); }
  .masthead-rule { position: absolute; left: 0; top: 150px; width: 927px; height: 2px; background: var(--white); }
  .title-art { position: absolute; left: 140px; top: 60px; width: 159px; height: 77px; background: linear-gradient(to bottom, var(--teal-pale), var(--teal)); }
  .title-number { position: absolute; left: 36px; top: 32px; color: var(--white); font-weight: 700; font-size: 128px; line-height: 1; letter-spacing: -12px; }
  .title-word { position: absolute; left: 154px; top: 72px; color: var(--navy); font-weight: 700; font-size: 46px; line-height: 1; }
  .headline { position: absolute; left: 363px; top: 34px; color: var(--white); font-weight: 700; line-height: 1; white-space: nowrap; }
  .headline-top { font-size: 42px; letter-spacing: -0.2px; }
  .headline-bottom { margin-top: 4px; font-size: 57px; letter-spacing: -0.3px; }
  .headline-bottom small { font-size: 36px; }

  .intro { position: absolute; left: 30px; top: 176px; width: 867px; text-align: center; font-size: 19.5px; line-height: 23.6px; }
  .intro-emphasis { position: absolute; left: 30px; top: 225px; width: 867px; text-align: center; font-weight: 700; font-size: 21.4px; line-height: 29px; }
  .intro-emphasis strong { font-size: 23.8px; }

  .signs-panel { position: absolute; left: 24px; top: 300px; width: 879px; height: 640px; border: 1.5px solid var(--navy); border-radius: 18px; background: linear-gradient(to bottom, var(--white) 0%, var(--teal-light) 45%, var(--teal) 100%); }

  .sign { position: absolute; font-size: 19.5px; line-height: 23.6px; }
  .sign-number { position: absolute; width: 36px; height: 36px; border-radius: 50%; background: var(--navy); color: var(--white); font-weight: 700; font-size: 28px; line-height: 36px; text-align: center; }
  .sign-title { font-weight: 700; font-size: 21px; line-height: 26px; }
  .sign-right .sign-title { margin-bottom: 4px; }
  .sign ul { list-style: none; }
  .sign li { position: relative; padding-left: 13px; }
  .sign li::before { content: "•"; position: absolute; left: 0; }

  .partner-tab { position: absolute; left: 41px; top: 876px; width: 397px; height: 60px; background: var(--navy); border-radius: 16px 16px 0 0; display: flex; align-items: center; padding-left: 22px; gap: 12px; }
  .partner-dot { width: 36px; height: 36px; border-radius: 50%; background: var(--teal); flex: none; }
  .partner-name { color: var(--teal); font-weight: 700; font-size: 18px; line-height: 20px; }

  .key-points { position: absolute; left: 0; top: 923px; width: 927px; height: 140px; background: var(--navy); }
  .key-points ul { list-style: none; position: absolute; left: 38px; top: 29px; color: var(--white); font-size: 19px; line-height: 24.3px; }
  .key-points li { display: flex; align-items: center; gap: 8px; white-space: nowrap; }
  .tick { width: 16px; height: 16px; flex: none; }

  .org-mark { position: absolute; left: 49px; top: 1078px; width: 125px; }
  .org-square { display: block; width: 24px; height: 24px; background: var(--teal); margin-bottom: 8px; }
  .org-name { display: block; font-weight: 700; font-size: 16px; line-height: 18px; color: var(--accent); }

  .learn-more { position: absolute; left: 202px; top: 1075px; font-size: 19px; line-height: 23px; white-space: nowrap; }
  .learn-more .link { font-weight: 700; font-size: 23px; line-height: 28.6px; }

  .logo-slot { position: absolute; left: 616px; top: 1074px; width: 282px; height: 105px; background: var(--slot); display: flex; align-items: center; justify-content: center; color: var(--slot-text); font-size: 23px; }
</style>
</head>
<body>
<div class="flyer">

  <header class="masthead">
    <div class="title-art" role="img" aria-label="Decorative title artwork behind the word Signs"></div>
    <div class="title-number">10</div>
    <div class="title-word">Signs</div>
    <div class="headline">
      <div class="headline-top">of Thinking or Memory Changes</div>
      <div class="headline-bottom"><small>that </small>Might be Dementia</div>
    </div>
    <div class="masthead-rule"></div>
  </header>

  <p class="intro">As we get older, we may slow down a bit. This is a normal part of aging. Changes in memory or thinking that make it harder to get through the day, are not a normal part of aging. These may be early signs of dementia.</p>
  <p class="intro-emphasis">Because American Indian and Alaska Native people have a high risk of dementia, it is important<br>to know the warning signs. <strong>Do you have any of these 10 signs? If so, talk to your doctor.</strong></p>

  <section class="signs-panel" aria-label="Ten warning signs"></section>

  <div class="sign-number" style="left:33px;top:310px">1</div>
  <div class="sign" style="left:75px;top:313px;width:362px">
    <div class="sign-title">Memory loss that affects your daily life.</div>
    You may:
    <ul><li>Forget events or important dates</li><li>Repeat yourself</li></ul>
    • Rely more often on lists or sticky notes to remember things
  </div>

  <div class="sign-number" style="left:33px;top:463px">2</div>
  <div class="sign" style="left:74px;top:466px;width:362px">
    <div class="sign-title">Trouble planning or solving problems.</div>
    You may have a harder time:
    <ul><li>Paying bills</li><li>Cooking recipes you have used for years</li></ul>
  </div>

  <div class="sign-number" style="left:33px;top:568px">3</div>
  <div class="sign" style="left:76px;top:571px;width:362px">
    <div class="sign-title">Get confused about the<br>time, date, or where you are.</div>
  </div>

  <div class="sign-number" style="left:33px;top:631px">4</div>
  <div class="sign" style="left:75px;top:635px;width:362px">
    <div class="sign-title">Daily tasks are getting harder,</div>
    Including:
    <ul><li>Driving</li><li>Making a grocery list or going shopping</li></ul>
  </div>

  <div class="sign-number" style="left:33px;top:741px">5</div>
  <div class="sign" style="left:75px;top:743px;width:370px">
    <div class="sign-title" style="width:340px">Trouble with how your eyesight and thinking work together that gets worse.</div>
    This includes:
    <ul><li>Tripping, falls, or problems with your balance</li><li>Spilling or dropping things more</li></ul>
  </div>

  <div class="sign-number" style="left:453px;top:310px">6</div>
  <div class="sign sign-right" style="left:499px;top:313px;width:400px">
    <div class="sign-title">New trouble talking or writing.</div>
    You have a hard time finding the words you want to say. For example, you may say “that thing on your wrist that tells time” instead of “watch.”
  </div>

  <div class="sign-number" style="left:453px;top:427px">7</div>
  <div class="sign sign-right" style="left:499px;top:431px;width:400px">
    <div class="sign-title">Lose and cannot find things.</div>
    For example, you:
    <ul><li>Can’t find the coffee pot that you use every day</li><li>Might put your car keys in the freezer</li></ul>
  </div>

  <div class="sign-number" style="left:453px;top:538px">8</div>
  <div class="sign sign-right" style="left:499px;top:540px;width:400px">
    <div class="sign-title">Notice changes in mood or personality</div>
    Such as being:
    <ul><li>Easily mad or sad in everyday situations</li><li>More fearful (scared) or suspicious (not trusting)</li></ul>
  </div>

  <div class="sign-number" style="left:453px;top:647px">9</div>
  <div class="sign sign-right" style="left:499px;top:650px;width:402px">
    <div class="sign-title" style="margin-left:3px">Act different and make poor choices.</div>
    This may make you more likely to:
    <ul><li>Spend money you do not have or be a scam victim</li><li>Stop washing up regularly or pay less attention to how you look</li><li>Forget to take care of your pet</li></ul>
  </div>

  <div class="sign-number" style="left:453px;top:809px;font-size:26px;letter-spacing:-1px">10</div>
  <div class="sign" style="left:495px;top:812px;width:390px">
    <div class="sign-title" style="margin-left:4px;width:385px">Pull away from friends and family because it is harder to keep up.</div>
    You may not want to do things you used to enjoy, like sporting events, church, music, or sex.
  </div>

  <div class="partner-tab">
    <span class="partner-dot"></span>
    <span class="partner-name">CEDAR PATH CENTER<br>FOR ELDER BRAIN HEALTH</span>
  </div>

  <section class="key-points">
    <ul>
      <li><svg class="tick" viewBox="0 0 16 16" aria-hidden="true"><path d="M2 9 L6 13 L14 2" fill="none" stroke="#4fa8b1" stroke-width="3"/></svg>American Indian and Alaska Native people have a high risk of dementia.</li>
      <li><svg class="tick" viewBox="0 0 16 16" aria-hidden="true"><path d="M2 9 L6 13 L14 2" fill="none" stroke="#4fa8b1" stroke-width="3"/></svg>Big changes in memory or thinking that make it hard to get through the day are not a normal part of aging.</li>
      <li><svg class="tick" viewBox="0 0 16 16" aria-hidden="true"><path d="M2 9 L6 13 L14 2" fill="none" stroke="#4fa8b1" stroke-width="3"/></svg>People with one or more of these 10 signs should talk to their doctor to find the cause. It is not always dementia.</li>
      <li><svg class="tick" viewBox="0 0 16 16" aria-hidden="true"><path d="M2 9 L6 13 L14 2" fill="none" stroke="#4fa8b1" stroke-width="3"/></svg>Early dementia diagnosis gives you a chance to get care and plan your future.</li>
    </ul>
  </section>

  <div class="org-mark">
    <span class="org-square"></span>
    <span class="org-name">RIVERSTONE ELDER WELLNESS ALLIANCE</span>
  </div>

  <div class="learn-more">
    To learn more about the warning signs of dementia<br>
    in American Indian and Alaska Native people, visit:
    <div class="link">www.cedarpathbrain.org</div>
    <div class="link">www.elderhealthinfo.org/aging</div>
  </div>

  <div class="logo-slot">Logo space</div>
</div>
</body>
</html>
```